I need a sophisticated and powerful book cover design that combines Japanese minimalism with contemporary appeal. The cover should convey personal transformation through the metaphor of a katana (Japanese sword).
Key Design Elements:
A katana, either partially shown or artistically rendered
Subtle Japanese design elements without being stereotypical
Clean, minimalist aesthetic
Professional font selection that bridges Eastern and Western typography
Color scheme: Deep blacks, steel grays, and possibly a touch of red or gold for accent
Mood/Style:
Professional and sophisticated
Blend of traditional Japanese aesthetics with modern design
Should appeal to personal development and business readers
Must convey strength and transformation
Elegant rather than aggressive
Specific Requirements:
Title: "The Lantern Compass"
Subtitle: "Quiet Practices for Growing Inner Steadiness and Calm Endurance Daily"
Author names: Moheshan Tadeli and Veena Tadeli
Cover dimensions: Standard hardcover book size (6" x 9")
Must work well in both physical and digital thumbnail formats
Should be striking and legible when viewed as a small image online
Design Specifics:
Japanese elements such as brushstroke effects, kanji characters, or wave patterns
The design should reflect the book's core message: personal transformation through Japanese wisdom principles, using the katana as a metaphor for growth and development.
Colors
Look and feel

```html
<!DOCTYPE html>
<html lang="en">
<head>
<meta charset="utf-8">
<title>The Lantern Compass — Book Cover</title>
<link rel="stylesheet" href="https://fonts.googleapis.com/css2?family=Russo+One&family=Poppins:wght@500;600&display=swap">
<style>
  :root {
    --backdrop: #8f8f8f;
    --paper: #ffffff;
    --ink: #0b0b0b;
    --accent-red: #f42a2a;
    --sun-red: #f2231e;
    --sun-soft: #ff5a4e;
  }
  * { margin: 0; padding: 0; box-sizing: border-box; }
  html, body {
    width: 1200px;
    height: 1200px;
    overflow: hidden;
    background: var(--backdrop);
  }
  .cover {
    position: absolute;
    left: 200px;
    top: 0;
    width: 800px;
    height: 1200px;
    background: var(--paper);
  }
  .title-block {
    position: absolute;
    left: 0;
    top: 0;
    width: 800px;
    height: 300px;
  }
  .title-line {
    font-family: "Russo One", "Arial Black", sans-serif;
    font-size: 124px;
  }
  .title-main { fill: var(--ink); }
  .title-accent { fill: var(--accent-red); }
  .subtitle {
    font-family: "Poppins", "Helvetica Neue", Arial, sans-serif;
    font-weight: 500;
    font-size: 29px;
    fill: var(--ink);
    text-transform: uppercase;
  }
  .artwork {
    position: absolute;
    left: 0;
    top: 470px;
    width: 800px;
    height: 530px;
    background:
      radial-gradient(circle 245px at 400px 278px, var(--sun-red) 0%, var(--sun-soft) 96%, rgba(255,255,255,0) 100%),
      var(--paper);
  }
  .authors {
    position: absolute;
    left: 0;
    top: 1100px;
    width: 800px;
    height: 60px;
  }
  .author-name {
    font-family: "Poppins", "Helvetica Neue", Arial, sans-serif;
    font-weight: 600;
    font-size: 36px;
    fill: var(--ink);
  }
  .author-join {
    font-family: "Poppins", "Helvetica Neue", Arial, sans-serif;
    font-weight: 600;
    font-size: 22px;
    fill: var(--accent-red);
  }
</style>
</head>
<body>
  <main class="cover">
    <svg class="title-block" viewBox="0 0 800 300" xmlns="http://www.w3.org/2000/svg">
      <text class="title-line title-main" x="42" y="184" textLength="717" lengthAdjust="spacingAndGlyphs">THE LANTERN</text>
      <text class="title-line title-accent" x="141" y="292" textLength="520" lengthAdjust="spacingAndGlyphs">COMPASS</text>
    </svg>

    <svg class="title-block" style="top:300px;height:120px" viewBox="0 0 800 120" xmlns="http://www.w3.org/2000/svg">
      <text class="subtitle" x="110" y="68" textLength="580" lengthAdjust="spacingAndGlyphs">Quiet Practices for Growing Inner</text>
      <text class="subtitle" x="35" y="109" textLength="730" lengthAdjust="spacingAndGlyphs">Steadiness and Calm Endurance Daily</text>
    </svg>

    <div class="artwork" role="img" aria-label="Illustration of a curved sword with gold-flecked blade laid across a red brushed sun, framed by branches of pink cherry blossom"></div>

    <svg class="authors" viewBox="0 0 800 60" xmlns="http://www.w3.org/2000/svg">
      <text x="400" y="42" text-anchor="middle">
        <tspan class="author-name">MOHESHAN TADELI</tspan>
        <tspan class="author-join" dx="6">AND</tspan>
        <tspan class="author-name" dx="6">VEENA TADELI</tspan>
      </text>
    </svg>
  </main>
</body>
</html>
```